Briefpapier für Hausarztpraxis
Zielgruppe
Briefkpapier für Hausarztpraxis - Zielgruppe von jung bis alt
Aufgabenstellung
Das Praxislogo sollte drauf sein,
Adresse ( Falkweidenweg 14, 72419 Morsbach OT Tiefenau ) , Name: Dr. Henrike Saalfeld Fachärztin für Allgemeinmedizin, Telefon 07145/6817, Website: hausarztpraxis-tiefenau.de , IBAN DE 4172 5840 0961 3357 18 Talgrundbank Morsbach•Lindau•Weilbrunn
Farbe entsprechend dem Logo

```html
<!DOCTYPE html>
<html lang="de">
<head>
<meta charset="utf-8">
<title>Briefpapier Hausarztpraxis Saalfeld</title>
<link rel="stylesheet" href="https://fonts.googleapis.com/css2?family=Libre+Franklin:wght@400&family=Open+Sans:wght@400;600;700&display=swap">
<style>
  :root {
    --crimson: #b5174f;
    --ink: #1f1f1f;
    --grey-rule: #8a8a8a;
    --paper: #f1f1f1;
    --backdrop: #dcdbdc;
    --ghost: #e4e4e4;
  }
  * { margin: 0; padding: 0; box-sizing: border-box; }
  html, body { width: 1119px; height: 1200px; overflow: hidden; background: var(--backdrop); }
  .letterhead {
    position: absolute; left: 148px; top: 20px; width: 823px; height: 1160px;
    background: var(--paper); overflow: hidden;
    font-family: "Libre Franklin", Arial, sans-serif; color: var(--ink);
  }
  .ghost-ring { position: absolute; left: 0; top: 0; width: 823px; height: 1160px; }
  .brand {
    position: absolute; left: 297px; top: 46px; width: 241px; text-align: center;
    font-family: "Open Sans", sans-serif; font-weight: 600; color: var(--crimson);
  }
  .brand-dot { display: block; width: 44px; height: 44px; border-radius: 50%; background: var(--crimson); margin: 0 auto 12px; }
  .brand-name { font-size: 14px; letter-spacing: 0.4px; line-height: 1.2; }
  .contact {
    position: absolute; left: 620px; top: 38px; width: 190px; font-style: normal;
    font-family: "Open Sans", sans-serif; font-size: 9.4px; line-height: 13.2px; color: var(--ink);
  }
  .contact-practice { font-size: 13px; line-height: 15px; color: var(--crimson); }
  .contact-doctor { font-size: 10.6px; line-height: 13px; color: var(--crimson); }
  .contact-title { font-size: 8.2px; line-height: 11px; }
  .contact-rule { width: 126px; height: 1px; background: var(--crimson); margin: 4px 0 8px; }
  .contact-line { display: flex; align-items: center; gap: 4px; }
  .contact-line svg { width: 8px; height: 8px; fill: var(--crimson); }
  .contact-bank { margin-top: 6px; }
  .sender-line {
    position: absolute; left: 79px; top: 211px;
    font-family: "Open Sans", sans-serif; font-size: 6.6px; color: var(--ink);
  }
  .sender-line .sender-name { color: var(--crimson); }
  .recipient { position: absolute; left: 80px; top: 264px; font-family: "Open Sans", sans-serif; font-size: 13px; line-height: 18px; }
  .letter-body { position: absolute; left: 81px; top: 436px; width: 618px; font-size: 15.4px; line-height: 20px; }
  .letter-body p { margin-bottom: 20px; }
  .signature-area { position: absolute; left: 92px; top: 846px; width: 136px; height: 56px; background: #e6e6e6; border-radius: 4px; }
  .footer-seal { position: absolute; left: 675px; top: 1049px; width: 64px; height: 64px; border-radius: 50%; border: 4px solid var(--crimson); background: var(--paper); }
  .footer-rule { position: absolute; left: 0; top: 1126px; width: 100%; height: 2px; background: var(--grey-rule); }
  .footer-band {
    position: absolute; left: 0; top: 1131px; width: 100%; height: 29px; background: var(--crimson);
    font-family: "Open Sans", sans-serif; font-weight: 700; font-size: 11px; color: #fff;
    text-align: right; padding-right: 33px; line-height: 29px;
  }
</style>
</head>
<body>
<main class="letterhead">
  <svg class="ghost-ring" viewBox="0 0 823 1160" aria-hidden="true">
    <circle cx="673" cy="990" r="250" fill="none" stroke="var(--ghost)" stroke-width="26"/>
  </svg>

  <div class="brand">
    <span class="brand-dot"></span>
    <div class="brand-name">Hausarztpraxis<br>Dr. med. Henrike Saalfeld</div>
  </div>

  <address class="contact">
    <div class="contact-practice">HAUSARZTPRAXIS</div>
    <div class="contact-doctor">Dr. Henrike Saalfeld</div>
    <div class="contact-title">Fachärztin für Allgemeinmedizin</div>
    <div class="contact-rule"></div>
    <div>Falkweidenweg 14</div>
    <div>72419 Morsbach OT Tiefenau</div>
    <div class="contact-line"><svg viewBox="0 0 10 10"><path d="M2 0l2 2-1 2c1 1 2 2 3 3l2-1 2 2-2 2C4 10 0 6 0 2z"/></svg>07145/6817</div>
    <div class="contact-line"><svg viewBox="0 0 10 10"><rect x="2" y="0" width="6" height="3"/><rect x="0" y="3" width="10" height="4" rx="1"/><rect x="2" y="6" width="6" height="4"/></svg>07145/6829</div>
    <div class="contact-bank">Bankverbindung:</div>
    <div>Talgrundbank Morsbach</div>
    <div>Lindau I Weilbrunn</div>
    <div>IBAN DE 4172 5840 0961 3357 18</div>
    <div>BIC: TLGBDE61TFN</div>
  </address>

  <div class="sender-line"><span class="sender-name">DR. HENRIKE SAALFELD</span> I Falkweidenweg 14, 72419 Morsbach OT Tiefenau</div>

  <div class="recipient">Herrn<br>Max Mustermann<br>Musterstrasse</div>

  <section class="letter-body">
    <p>Dear Valued Customer:</p>
    <p>Our records show that you have been a customer of Harbor Lane Outfitters. since our grand opening last year. We would like to thank you for your business by inviting you to our preferred customer Spring Extravaganza next Saturday.</p>
    <p>Saturday's sales event is by invitation only. All of our stock, ................................and bedding will be marked down from 50-80% off.* Doors open at 9:00 AM sharp. Complimentary coffee and donuts will be served. Public admission will commence at noon.</p>
    <p>In addition, please accept the enclosed $10 gift certificate to use with your purchase of $75 or more.</p>
    <p>We look forward to seeing you on Saturday. Please bring this invitation with you and present it at the door.</p>
    <p>Sincerely,</p>
  </section>

  <div class="signature-area" role="img" aria-label="Handschriftliche Unterschrift"></div>

  <div class="footer-seal"></div>
  <div class="footer-rule"></div>
  <div class="footer-band">www.hausarztpraxis-tiefenau.de</div>
</main>
</body>
</html>
```